New flyer design for construction company marketing and description of services.

I want to have a flyer design that my techs will carry to deliver after job completion or for marketing purposes, to explain what services we provide, we offer General construction services.

Brightnail Handyman Sevices originated from a family-owned and operated contractor business, performing home renovation, addition, and construction work in the NYC area since 2004.

Today, we specialize in reliable and affordable Construction services for residential and commercial clients In 2014, we expanded to northern New Jersey. In 2016, we brought quality home improvement and repair services to new Bucks County, PA, and nearby New Jersey areas.
We offer carpentry, electrical, plumbing, renovation, remodel, cleaning services and landscaping.
I would like to have a section for home rental maintenance.

Target Market(s)

Homeowners, rental properties, real state and Senior citizen

Industry/Entity Type

Construction Company

Colors

Designer to choose colors to be used in the design.

Requirements
Must have
• A special design that will attract 55 + clients maybe a logo version that will be more attractive to seniors. I would updated the briefing with design and previous pictures, but we have all available in our social media instagram and facebook:
• https://www.sampleinsta.test/brightnailhandyman/?hl=en
• https://www.samplefacebook.test/brightnailhandy/
Nice to have
• New design ideas and layouts.

```html
<!DOCTYPE html>
<html lang="en">
<head>
<meta charset="utf-8">
<title>Brightnail Handyman Services – Flyers</title>
<link rel="stylesheet" href="https://fonts.googleapis.com/css2?family=Bebas+Neue&family=Open+Sans:wght@400;600&family=Signika:wght@400;500;600;700&display=swap">
<style>
  :root{
    --page:#e9eaeb;
    --red:#c4161c;
    --red-dark:#8e0f14;
    --ink:#1b1b1b;
    --grey:#555;
    --wood-light:#e2cdb0;
    --wood-dark:#c9ac88;
    --yellow:#f6d60c;
    --black:#111;
    --white:#fff;
  }
  *{box-sizing:border-box;margin:0;padding:0}
  html,body{width:1200px;height:785px;overflow:hidden;background:var(--page)}
  body{position:relative;font-family:"Signika",sans-serif;color:var(--ink)}

  .flyer{position:absolute;top:63px;width:503px;height:651px;background:var(--white);overflow:hidden;box-shadow:0 3px 8px rgba(0,0,0,.28)}
  .flyer--about{left:62px}
  .flyer--services{left:609px}

  .hero-photo{position:absolute;top:19px;height:308px;right:0}
  .flyer--about .hero-photo{left:230px;background:linear-gradient(160deg,#f1ece4 0%,#d9cbb8 40%,#2d3650 62%,#1f2840 100%)}
  .flyer--services .hero-photo{left:238px;background:linear-gradient(150deg,#dcdad6 0%,#b9b5ae 35%,#f0a11c 55%,#2a3150 75%,#1b2038 100%)}

  .hero-shapes{position:absolute;left:0;top:0;width:503px;height:327px}

  .brand{position:absolute;left:16px;top:34px;display:flex;align-items:center;gap:8px}
  .brand__dot{width:44px;height:44px;border-radius:50%;background:var(--red)}
  .brand__name{font-family:"Signika",sans-serif;font-weight:700;font-size:36px;line-height:1;color:var(--ink)}
  .brand__tag{position:absolute;left:90px;top:88px;font-size:8px;letter-spacing:2.6px;color:var(--grey);white-space:nowrap}

  .headline{position:absolute;left:16px;top:168px;font-family:"Bebas Neue",sans-serif;font-size:41px;line-height:43.5px;color:var(--ink)}
  .flyer--services .headline{font-size:35px;left:17px}
  .subline{position:absolute;left:16px;top:255px;font-size:13px;line-height:15.6px;color:var(--red);white-space:nowrap}
  .flyer--services .subline{left:17px}

  .wood{position:absolute;left:0;top:327px;width:503px;height:324px;background:linear-gradient(90deg,var(--wood-light) 0%,#d8c09f 30%,var(--wood-light) 55%,var(--wood-dark) 100%)}

  .intro{position:absolute;left:16px;top:340px;width:470px;font-family:"Open Sans",sans-serif;font-weight:600;font-size:9.6px;line-height:14px;letter-spacing:-.15px;text-align:justify;color:var(--ink)}

  .service-grid{position:absolute;left:18px;top:430px;width:468px;height:158px;background:rgba(255,255,255,.93);display:grid;grid-template-columns:1fr 1fr;grid-template-rows:1fr 1fr}
  .service{position:relative;padding:16px 8px 0 81px}
  .service:nth-child(1),.service:nth-child(3){border-right:1px dotted #999}
  .service:nth-child(1),.service:nth-child(2){border-bottom:1px dotted #999}
  .service__icon{position:absolute;left:7px;top:11px;width:43px;height:50px}
  .service__title{font-family:"Bebas Neue",sans-serif;font-size:15px;line-height:15px;color:var(--red);margin-bottom:3px}
  .service__text{font-size:6.6px;line-height:8px;color:var(--ink);text-align:justify;width:142px}

  .offer-title{position:absolute;left:17px;top:340px;font-family:"Bebas Neue",sans-serif;font-size:25px;line-height:26px;color:var(--ink)}
  .offer-list{position:absolute;left:17px;top:374px;list-style:none}
  .offer-list li{position:relative;padding-left:22px;font-size:12.8px;line-height:19.3px;font-weight:500;color:var(--ink)}
  .offer-list li::before{content:"";position:absolute;left:0;top:5px;width:10px;height:10px;border:1.5px solid var(--red);border-radius:2px}
  .offer-list li::after{content:"";position:absolute;left:4px;top:3px;width:5px;height:9px;border-right:2px solid var(--red);border-bottom:2px solid var(--red);transform:rotate(40deg)}

  .gallery{position:absolute;left:227px;top:338px;display:grid;grid-template-columns:124px 125px;grid-auto-rows:80px;column-gap:7px;row-gap:10px}
  .shot{position:relative;overflow:hidden}
  .shot--before{background:linear-gradient(135deg,#c9c2b6,#7a5a3f 60%,#4a3a2c)}
  .shot--after{background:linear-gradient(135deg,#e7dfd2,#b58a5a 55%,#6a2f20)}
  .shot__tag{position:absolute;left:-18px;top:10px;width:72px;transform:rotate(-35deg);background:var(--red);color:var(--white);font-size:7px;font-weight:700;text-align:center;line-height:11px;letter-spacing:.3px}

  .footer-yellow{position:absolute;left:0;top:615px;width:310px;height:36px;background:var(--yellow)}
  .footer-yellow::before{content:"";position:absolute;left:0;top:0;right:0;height:7px;background:repeating-linear-gradient(90deg,rgba(0,0,0,.35) 0 1px,transparent 1px 4px)}
  .footer-contact{position:absolute;left:18px;top:629px;font-size:10px;line-height:14px;color:var(--ink);white-space:nowrap}
  .footer-phone{position:absolute;left:0;top:607px;width:503px;height:44px}
  .phone{position:absolute;left:342px;top:615px;font-size:21px;line-height:28px;color:var(--white);letter-spacing:.5px;white-space:nowrap}
</style>
</head>
<body>

<section class="flyer flyer--about">
  <div class="hero-photo" role="img" aria-label="Smiling handyman in hard hat and work gloves standing with arms crossed in a bright interior"></div>
  <svg class="hero-shapes" viewBox="0 0 503 327" aria-hidden="true">
    <defs>
      <linearGradient id="bandA" x1="0" y1="0" x2="0" y2="1">
        <stop offset="0" stop-color="#b01218"/><stop offset="1" stop-color="#8e0f14"/>
      </linearGradient>
    </defs>
    <polygon points="0,117 300,117 276,327 0,327" fill="url(#bandA)"/>
    <polygon points="0,149 280,149 308,307 0,307" fill="#fff"/>
  </svg>

  <div class="brand"><span class="brand__dot"></span><span class="brand__name">Brightnail</span></div>
  <div class="brand__tag">HANDYMAN SERVICES</div>

  <h1 class="headline">A BETTER WAY<br>TO GET TASK DONE</h1>
  <p class="subline">Licensed Home Improvement Contractor in<br>PA 100245 and NJ 13VH00482100</p>

  <div class="wood"></div>
  <p class="intro">Brightnail Handyman Sevices originated from a family-owned and operated contractor business, performing home renovation, addition, and construction work in the NYC area since 2004. Today, we specialize in reliable and affordable Construction services for residential and commercial clients In 2014, we expanded to northern New Jersey. In 2016, we brought quality home improvement and repair services to new Bucks County, PA, and nearby New Jersey areas.</p>

  <div class="service-grid">
    <div class="service">
      <svg class="service__icon" viewBox="0 0 43 50" aria-hidden="true"><polygon points="21.5,2 41,13 41,37 21.5,48 2,37 2,13" fill="#fff" stroke="#333" stroke-width="1.5"/><circle cx="21.5" cy="19" r="6" fill="#c4161c"/><path d="M11 36c0-7 5-10 10.5-10S32 29 32 36z" fill="#c4161c"/></svg>
      <h2 class="service__title">GENERAL CONTRACTOR</h2>
      <p class="service__text">We are committed to our clients in offering them products and services of first-class quality, within the timelines and budgets agreed.</p>
    </div>
    <div class="service">
      <svg class="service__icon" viewBox="0 0 43 50" aria-hidden="true"><polygon points="21.5,2 41,13 41,37 21.5,48 2,37 2,13" fill="#fff" stroke="#333" stroke-width="1.5"/><polygon points="13,20 30,20 27,36 16,36" fill="#c4161c"/><rect x="24" y="11" width="2.5" height="12" fill="#c4161c"/></svg>
      <h2 class="service__title">CLEANING SERVICES</h2>
      <p class="service__text">If you're in need of home cleaning, apartment cleaning, or a maid service, we're simply the best, most convenient home cleaning service out there.</p>
    </div>
    <div class="service">
      <svg class="service__icon" viewBox="0 0 43 50" aria-hidden="true"><polygon points="21.5,2 41,13 41,37 21.5,48 2,37 2,13" fill="#fff" stroke="#333" stroke-width="1.5"/><polygon points="21.5,13 33,24 30,24 30,36 13,36 13,24 10,24" fill="#c4161c"/></svg>
      <h2 class="service__title">PROPERTY MAINTENANCE</h2>
      <p class="service__text">Whether your facility is large or small, we are responsible for fixing damage and replacing equipment, as well as replenishing any supplies necessary for the efficient operation of the property.</p>
    </div>
    <div class="service">
      <svg class="service__icon" viewBox="0 0 43 50" aria-hidden="true"><polygon points="21.5,2 41,13 41,37 21.5,48 2,37 2,13" fill="#fff" stroke="#333" stroke-width="1.5"/><circle cx="21.5" cy="25" r="7" fill="none" stroke="#c4161c" stroke-width="5" stroke-dasharray="3 2.5"/><circle cx="21.5" cy="25" r="5" fill="none" stroke="#c4161c" stroke-width="3"/></svg>
      <h2 class="service__title">HANDYMAN SERVICES</h2>
      <p class="service__text">If you're looking for the best handyman service to help you out around the house, look no further. We know you've got a never-ending list of odd jobs that need doing around your home.</p>
    </div>
  </div>

  <div class="footer-yellow"></div>
  <p class="footer-contact">brightnailhandymannyc@mail.test | www.brightnail.test</p>
  <svg class="footer-phone" viewBox="0 0 503 44" aria-hidden="true">
    <polygon points="296,0 503,0 503,44 282,44" fill="#111"/>
    <circle cx="320" cy="22" r="11" fill="none" stroke="#fff" stroke-width="2"/>
    <path d="M315 16c1-1 2-1 3 0l1.5 2.5c.4.8 0 1.5-.6 2 .8 1.8 2 3 3.8 3.8.5-.6 1.2-1 2-.6l2.5 1.5c1 1 1 2 0 3-2 2-5 1-8-2s-4-6-2-8z" fill="#fff"/>
  </svg>
  <p class="phone">(215) 555-0148</p>
</section>

<section class="flyer flyer--services">
  <div class="hero-photo" role="img" aria-label="Handyman holding a hammer and hard hat with a tool belt in front of a house entrance"></div>
  <svg class="hero-shapes" viewBox="0 0 503 327" aria-hidden="true">
    <defs>
      <linearGradient id="bandB" x1="0" y1="0" x2="0" y2="1">
        <stop offset="0" stop-color="#b01218"/><stop offset="1" stop-color="#8e0f14"/>
      </linearGradient>
    </defs>
    <polygon points="0,117 336,117 300,327 0,327" fill="url(#bandB)"/>
    <polygon points="0,149 279,149 332,307 0,307" fill="#fff"/>
  </svg>

  <div class="brand"><span class="brand__dot"></span><span class="brand__name">Brightnail</span></div>
  <div class="brand__tag">HANDYMAN SERVICES</div>

  <h1 class="headline">BRIGHTNAIL HANDYMAN<br>SERVICES</h1>
  <p class="subline">CALLTHE PROS, NOT THE CONS<br>WE DO IT ALL, LARGE AND SMALL</p>

  <div class="wood"></div>
  <h2 class="offer-title">SERVICES WE OFFER</h2>
  <ul class="offer-list">
    <li>CARPENTRY</li>
    <li>ELECTRICAL</li>
    <li>PLUMBING</li>
    <li>RENOVATION</li>
    <li>REMODEL</li>
    <li>CLEANING SERVICES</li>
    <li>LANDSCAPING</li>
    <li>MAINTENANCE</li>
    <li>PAINTING</li>
    <li>WOOD TRIM</li>
    <li>TILE</li>
    <li>REPAIR</li>
  </ul>

  <div class="gallery">
    <div class="shot shot--before" role="img" aria-label="Kitchen before renovation"><span class="shot__tag">BEFORE</span></div>
    <div class="shot shot--after" role="img" aria-label="Kitchen after renovation"><span class="shot__tag">AFTER</span></div>
    <div class="shot shot--before" role="img" aria-label="Balcony before repair"><span class="shot__tag">BEFORE</span></div>
    <div class="shot shot--after" role="img" aria-label="Balcony after repair with new railing"><span class="shot__tag">AFTER</span></div>
    <div class="shot shot--before" role="img" aria-label="Basement before remodel"><span class="shot__tag">BEFORE</span></div>
    <div class="shot shot--after" role="img" aria-label="Finished basement after remodel"><span class="shot__tag">AFTER</span></div>
  </div>

  <div class="footer-yellow"></div>
  <p class="footer-contact">brightnailhandymannyc@mail.test | www.brightnail.test</p>
  <svg class="footer-phone" viewBox="0 0 503 44" aria-hidden="true">
    <polygon points="296,0 503,0 503,44 282,44" fill="#111"/>
    <circle cx="320" cy="22" r="11" fill="none" stroke="#fff" stroke-width="2"/>
    <path d="M315 16c1-1 2-1 3 0l1.5 2.5c.4.8 0 1.5-.6 2 .8 1.8 2 3 3.8 3.8.5-.6 1.2-1 2-.6l2.5 1.5c1 1 1 2 0 3-2 2-5 1-8-2s-4-6-2-8z" fill="#fff"/>
  </svg>
  <p class="phone">(215) 555-0148</p>
</section>

</body>
</html>
```